Email Design Creative Design Needed

Our website is called CampusLedger.org. One of our competitor(varsity scout.us.com) is using the following email creative.
http://qtr.brightvelmo.com/Affiliate/Assets/3532.html
http://qtr.brightvelmo.com/Affiliate/Assets/7921.html
http://qtr.brightvelmo.com/Affiliate/Assets/8061.html

We would like to use similar email creative without copying their exact creative. You can use the above as a guide but then come up with your own version of the creative.
The above are just concepts, please be creative and come up with your own version of it, without feeling that they have been copied. Feel free to move the components around. Also, feel free to change the colours and text.

Please find attached the CampusLedger.org logo.

Reason: We would like to receive more designs.

Industry/Entity Type

College

```html
<!DOCTYPE html>
<html lang="en">
<head>
<meta charset="utf-8">
<title>CampusLedger – Substance Abuse Counseling Degrees</title>
<link href="https://fonts.googleapis.com/css2?family=Open+Sans:ital,wght@0,400;0,600;0,700;1,400;1,600&display=swap" rel="stylesheet">
<style>
  :root {
    --page-bg: #3a2218;
    --card-bg: #ececec;
    --header-bg: #1f3535;
    --brand-lime: #c5d600;
    --ink: #1f2a2a;
    --ink-soft: #333;
    --link-green: #5a8a00;
    --photo-dark: #3c3c38;
    --photo-light: #b5b5ad;
    --label-bg: rgba(40,45,45,0.88);
    --btn-top: #ffd84a;
    --btn-bottom: #f2b200;
    --col-green: #0c4d3a;
    --col-yellow: #d3c800;
    --col-maroon: #7a2a4c;
    --white: #ffffff;
  }
  * { margin: 0; padding: 0; box-sizing: border-box; }
  html, body { width: 1200px; height: 1167px; overflow: hidden; }
  body {
    background: var(--page-bg);
    font-family: "Open Sans", Arial, sans-serif;
    position: relative;
  }
  .email-card {
    position: absolute; left: 280px; top: 49px;
    width: 649px; height: 1078px;
    background: var(--card-bg);
  }
  .view-note {
    position: absolute; top: 16px; width: 100%;
    text-align: center; font-size: 11px; color: var(--ink-soft);
  }
  .view-note a, .footer a { color: var(--link-green); }
  .content {
    position: absolute; left: 44px; top: 44px; width: 569px;
  }
  .masthead {
    height: 143px; background: var(--header-bg);
    position: relative;
  }
  .brand {
    position: absolute; left: 22px; top: 48px;
    display: flex; align-items: center; gap: 8px;
  }
  .brand-dot {
    width: 32px; height: 32px; border-radius: 50%;
    background: var(--brand-lime);
  }
  .brand-name {
    color: var(--brand-lime); font-weight: 700; font-size: 28px;
    letter-spacing: -0.5px;
  }
  .tagline {
    position: absolute; left: 327px; top: 44px; width: 230px;
    color: var(--white); font-style: italic; font-size: 15px; line-height: 18px;
  }
  .hero {
    height: 290px; position: relative;
    background: linear-gradient(160deg, var(--photo-light) 0%, #8d8d85 45%, var(--photo-dark) 100%);
  }
  .hero-label {
    position: absolute; right: 0; top: 199px;
    width: 272px; height: 59px; background: var(--label-bg);
    color: var(--white); text-align: center; padding-top: 6px;
  }
  .hero-label .lead { font-size: 20px; letter-spacing: -0.5px; line-height: 24px; }
  .hero-label .sub { font-size: 17px; font-style: italic; font-weight: 600; line-height: 22px; }
  .pitch {
    height: 259px; background: var(--white); text-align: center;
    position: relative;
  }
  .pitch-lead { padding-top: 48px; font-size: 20px; color: var(--ink); letter-spacing: -0.3px; }
  .pitch-title { font-size: 23px; font-weight: 700; color: var(--ink); margin-top: 2px; }
  .cta {
    position: absolute; left: 112px; top: 118px;
    width: 345px; height: 54px; border-radius: 6px;
    background: linear-gradient(var(--btn-top), var(--btn-bottom));
    box-shadow: 0 3px 4px rgba(0,0,0,0.25);
    color: var(--ink); font-size: 16px; line-height: 18px;
    display: flex; align-items: center;
  }
  .cta-text { flex: 1; text-align: center; padding-left: 10px; }
  .cta-icon { width: 34px; height: 34px; margin-right: 12px; }
  .pitch-rule {
    position: absolute; left: 10px; right: 10px; bottom: 36px; height: 1px;
    background: linear-gradient(90deg, transparent, #ccc, transparent);
  }
  .salary-table {
    width: 569px; border-collapse: collapse; table-layout: fixed;
    color: var(--white); text-align: center;
  }
  .salary-table th {
    height: 39px; font-size: 17px; font-weight: 600;
  }
  .salary-table td {
    height: 33px; font-size: 11.5px; line-height: 12px;
    border-top: 1px solid rgba(255,255,255,0.5);
  }
  .col-occupation { background: var(--col-green); }
  .col-salary { background: var(--col-yellow); font-weight: 700; color: var(--ink); }
  th.col-salary { color: var(--ink); }
  .col-steps { background: var(--col-maroon); }
  .salary-table td + td, .salary-table th + th { border-left: 1px solid rgba(255,255,255,0.6); }
  .table-note {
    height: 59px; background: var(--white);
    font-size: 10px; color: var(--ink-soft); text-align: center; padding-top: 6px;
  }
  .table-note u { color: var(--ink); }
  .footer {
    position: absolute; top: 1000px; width: 100%;
    text-align: center; color: var(--ink); font-size: 13px;
  }
  .footer .fine { font-size: 10px; line-height: 12px; margin-top: 10px; }
</style>
</head>
<body>
  <div class="email-card">
    <p class="view-note">Having problems viewing this email? <a href="#">Click here</a> to view in browser.</p>

    <div class="content">
      <header class="masthead">
        <div class="brand">
          <span class="brand-dot"></span>
          <span class="brand-name">CampusLedger</span>
        </div>
        <p class="tagline">"Higher Education opens the door, illuminates the path and guides us to the future."</p>
      </header>

      <section class="hero" role="img" aria-label="Grayscale photo of a young man lying curled on a worn floor beside scattered syringes">
        <div class="hero-label">
          <div class="lead">DEGREES IN PSYCHOLOGY</div>
          <div class="sub">Substance Abuse Counseling</div>
        </div>
      </section>

      <section class="pitch">
        <p class="pitch-lead">FIND OUT MORE ABOUT PSYCHOLOGY DEGREES</p>
        <p class="pitch-title">SUBSTANCE ABUSE COUNSELING</p>
        <a class="cta" href="#">
          <span class="cta-text">REQUEST FREE SUBSTANCE ABUSE<br>COUNSELING INFORMATION</span>
          <svg class="cta-icon" viewBox="0 0 34 34" aria-hidden="true">
            <circle cx="17" cy="17" r="16" fill="#f39a00"/>
            <path d="M9 14h9v-5l8 8-8 8v-5H9z" fill="#fff"/>
          </svg>
        </a>
        <div class="pitch-rule"></div>
      </section>

      <table class="salary-table">
        <thead>
          <tr>
            <th class="col-occupation">OCCUPATION TYPE</th>
            <th class="col-salary">MEDIAN SALARY*</th>
            <th class="col-steps">NEXT STEPS</th>
          </tr>
        </thead>
        <tbody>
          <tr>
            <td class="col-occupation">Substance Abuse and Behavioral Disorder Counselors</td>
            <td class="col-salary">$41,030/year</td>
            <td class="col-steps">Substance Abuse and Behavioral Disorder Counselors Programs</td>
          </tr>
          <tr>
            <td class="col-occupation">Mental Health and Substance Abuse Social Workers</td>
            <td class="col-salary">$42,650/year</td>
            <td class="col-steps">Mental Health and Substance Abuse</td>
          </tr>
          <tr>
            <td class="col-occupation">Rehabilitation Counselors</td>
            <td class="col-salary">$37,070/year</td>
            <td class="col-steps">Rehabilitation Counselors Programs</td>
          </tr>
          <tr>
            <td class="col-occupation">Mental Health Counselors</td>
            <td class="col-salary">$42,590/year</td>
            <td class="col-steps">Mental Health Counselors Programs</td>
          </tr>
        </tbody>
      </table>
      <p class="table-note">*Median salaries according to the <u>National Labor Data Office</u></p>
    </div>

    <footer class="footer">
      <p>Copyright © 2014 <strong>CampusLedger.org</strong> | All rights reserved</p>
      <p class="fine">You are receiving this email because you subscribed at <a href="#">www.campusledger.org</a>.<br>To unsubscribe, <a href="#">click here</a>.</p>
    </footer>
  </div>
</body>
</html>
```